velmora LED lighting Brochure design *

need a Brochure for velmora LED, that is a company specialises in industrial LED lighting solutions ... we also do retail, gas stations as well...
we are formed to serve customer need in lighting doing engineering, supply and installation of LED lighting
we need a Brochure that describe our company work, project cycle, project reference and services provided in addition to our main products that will be provided to consultant for product range approval

Target Market(s)

industrial sector (petrochemical, chemical, factories), construction, retail shops, gas stations

Industry/Entity Type

Lighting

Colors

Requirements
Must have
• project cycle
• project reference photos... cant upload it here

```html
<!DOCTYPE html>
<html lang="en">
<head>
<meta charset="utf-8">
<title>Velmora LED Lighting Brochure</title>
<link href="https://fonts.googleapis.com/css2?family=Montserrat:wght@400;600;700;800&display=swap" rel="stylesheet">
<style>
  :root {
    --navy: #1f3347;
    --coral: #e9546b;
    --blush: #f5a9b1;
    --sky: #8fd3e8;
    --ink: #3a4350;
    --muted: #8a929c;
    --paper: #ffffff;
    --backdrop: #eeeeef;
  }
  * { margin: 0; padding: 0; box-sizing: border-box; }
  html, body { width: 800px; height: 1200px; overflow: hidden; }
  body { background: var(--backdrop); font-family: 'Montserrat', sans-serif; color: var(--ink); position: relative; }

  .page {
    position: absolute; left: 220px; width: 360px; height: 252px;
    background: var(--paper); overflow: hidden;
    box-shadow: 0 3px 10px rgba(0,0,0,0.18);
  }
  .page--cover { top: 36px; }
  .page--back { top: 330px; }
  .page--about { top: 624px; }
  .page--product { top: 918px; }

  .abs { position: absolute; }
  .brand { font-weight: 800; font-size: 9px; letter-spacing: 1px; color: var(--navy); display: flex; align-items: center; gap: 4px; }
  .brand .mark { width: 7px; height: 7px; background: var(--coral); }
  .brand--light { color: #fff; }

  /* cover */
  .cover-band { left: 0; top: 0; width: 52px; height: 210px; background: var(--navy); }
  .cover-photo { left: 80px; top: 36px; width: 250px; height: 128px; background: linear-gradient(160deg, #4a5a6c 0%, #8c97a3 45%, #2b3a4a 100%); }
  .cover-stripes { right: 0; top: 0; width: 90px; height: 130px; }
  .cover-sky { left: 52px; top: 190px; width: 28px; height: 20px; background: var(--sky); }
  .cover-title { left: 80px; top: 178px; font-weight: 800; font-size: 11px; color: var(--navy); letter-spacing: 0.2px; }
  .cover-web { left: 80px; top: 195px; font-size: 6px; color: var(--muted); }

  /* back */
  .back-photo { left: 0; top: 0; width: 100%; height: 190px; background: linear-gradient(180deg, #f6f7f8 0%, #e7eaed 60%, #f3f4f5 100%); }
  .back-sky { left: 22px; top: 12px; width: 18px; height: 42px; background: var(--sky); }
  .back-band { left: 0; top: 196px; width: 100%; height: 36px; background: var(--navy); }
  .back-coral { right: 20px; top: 180px; width: 6px; height: 18px; background: var(--coral); }
  .back-blush { right: 26px; top: 188px; width: 30px; height: 8px; background: var(--blush); }
  .back-call { left: 130px; top: 203px; color: #fff; }
  .back-call small { display: block; font-size: 5px; letter-spacing: 1px; }
  .back-call strong { font-size: 10px; font-weight: 800; }
  .back-contacts { left: 240px; top: 201px; color: #fff; font-size: 4.5px; line-height: 7px; list-style: none; }
  .back-contacts li::before { content: ""; display: inline-block; width: 3px; height: 3px; background: var(--sky); margin-right: 3px; vertical-align: middle; }

  /* about */
  .about-photo { left: 0; top: 0; width: 150px; height: 100%; background: linear-gradient(180deg, #0c1422 0%, #1e2a3a 55%, #3a3a3c 100%); }
  .about-bar-sky { left: 150px; top: 22px; width: 8px; height: 70px; background: var(--sky); }
  .about-bar-blush { left: 158px; top: 40px; width: 8px; height: 90px; background: var(--blush); }
  .about-bar-coral { left: 166px; top: 30px; width: 4px; height: 60px; background: var(--coral); }
  .about-text { left: 190px; top: 40px; width: 150px; font-size: 4.6px; line-height: 6.4px; color: var(--ink); }
  .about-text p { margin-bottom: 5px; }
  .about-brand { left: 250px; top: 14px; }
  .page-num { font-size: 4.5px; color: var(--muted); }
  .about-num { right: 18px; bottom: 10px; }

  /* product */
  .product-sky { left: 16px; top: 14px; width: 36px; height: 12px; background: var(--sky); }
  .product-title { left: 16px; top: 42px; font-weight: 800; font-size: 14px; color: var(--navy); letter-spacing: 0.5px; }
  .product-desc { left: 16px; top: 62px; width: 100px; font-size: 4.5px; line-height: 6.2px; }
  .product-area { left: 16px; top: 100px; font-weight: 700; font-size: 5.5px; color: var(--navy); }
  .product-area-text { left: 16px; top: 109px; width: 100px; font-size: 4.5px; }
  .product-web { left: 16px; top: 132px; font-size: 4.5px; color: var(--muted); }
  .product-lamp { left: 130px; top: 40px; width: 110px; height: 110px; border-radius: 50%; background: radial-gradient(circle, #5a5f66 0%, #2c3036 60%, #1a1d21 100%); }
  .product-photo { left: 256px; top: 30px; width: 104px; height: 200px; background: linear-gradient(180deg, #9aa3ad 0%, #d9dde2 40%, #6d7680 100%); }
  .product-triangle { right: 0; top: 0; width: 104px; height: 60px; }
  .product-num { left: 200px; bottom: 10px; }
</style>
</head>
<body>

<section class="page page--cover">
  <div class="abs cover-band"></div>
  <div class="abs brand" style="left:62px;top:12px;"><span class="mark"></span>velmora</div>
  <div class="abs cover-photo" role="img" aria-label="Warehouse interior lit by LED highbay fixtures"></div>
  <svg class="abs cover-stripes" viewBox="0 0 90 130" aria-hidden="true">
    <polygon points="30,0 48,0 20,130 2,130" fill="#e9546b"/>
    <polygon points="56,0 72,0 44,130 28,130" fill="#f5a9b1"/>
    <polygon points="78,0 90,0 90,40 70,130 54,130" fill="#1f3347"/>
  </svg>
  <div class="abs cover-sky"></div>
  <div class="abs cover-title">VELMORA LIGHTING TECHNOLOGY CO. LTD.</div>
  <div class="abs cover-web">www.velmoraled.com</div>
</section>

<section class="page page--back">
  <div class="abs back-photo" role="img" aria-label="Faint photo of an industrial hall"></div>
  <div class="abs back-sky"></div>
  <div class="abs back-coral"></div>
  <div class="abs back-blush"></div>
  <div class="abs back-band"></div>
  <div class="abs brand brand--light" style="left:20px;top:209px;"><span class="mark"></span>velmora</div>
  <div class="abs back-call"><small>CALL US NOW</small><strong>000 12 3456789</strong></div>
  <ul class="abs back-contacts">
    <li>Building 12, Industrial Area</li>
    <li>info@velmoraled.com</li>
    <li>www.velmoraled.com</li>
  </ul>
</section>

<section class="page page--about">
  <div class="abs about-photo" role="img" aria-label="Street lights glowing at night"></div>
  <div class="abs about-bar-sky"></div>
  <div class="abs about-bar-blush"></div>
  <div class="abs about-bar-coral"></div>
  <div class="abs brand about-brand"><span class="mark"></span>velmora</div>
  <div class="abs about-text">
    <p>Velmora Lighting Technology is a trusted supplier of industrial LED lighting, serving plants and sites across the region.</p>
    <p>We deliver engineering, supply and installation with a focus on efficiency, safety and long service life.</p>
    <p>Our products are tested for harsh settings including petrochemical, chemical and factory environments.</p>
    <p>Every project follows a clear cycle: survey, design, approval, supply, installation and after-sales support.</p>
  </div>
  <div class="abs page-num about-num">Page 2</div>
</section>

<section class="page page--product">
  <div class="abs product-sky"></div>
  <div class="abs product-title">HIGHBAY</div>
  <div class="abs product-desc">Highbay fixtures are designed for industrial ceilings, delivering bright uniform light with low energy use.</div>
  <div class="abs product-area">AREA OF APPLICATION</div>
  <div class="abs product-area-text">Warehouses, factories, workshops and halls</div>
  <div class="abs product-web">www.velmoraled.com</div>
  <div class="abs product-lamp" role="img" aria-label="Round LED highbay fixture"></div>
  <div class="abs product-photo" role="img" aria-label="Factory hall lit by highbay lights"></div>
  <svg class="abs product-triangle" viewBox="0 0 104 60" aria-hidden="true">
    <polygon points="40,0 104,0 104,50" fill="#e9546b"/>
    <polygon points="70,0 104,0 104,22" fill="#f5a9b1"/>
  </svg>
  <div class="abs page-num product-num">Page 3</div>
</section>

</body>
</html>
```